Corvane Global Treks Facebook Page

I would like to have a very professional and unique Facebook page for my business
www.corvaneglobaltreks.com

```html
<!DOCTYPE html>
<html lang="en">
<head>
<meta charset="utf-8">
<title>Corvane Global Treks – Facebook Cover</title>
<link rel="stylesheet" href="https://fonts.googleapis.com/css2?family=Open+Sans:wght@300;400;700;800&display=swap">
<style>
  :root {
    --stage-bg: #e4e4e4;
    --teal-dark: #12759c;
    --teal-light: #2a8e9c;
    --sky-deep: #1c3f93;
    --sky-top: #2f5cb0;
    --sky-mid: #8aa8d6;
    --snow: #eef2f8;
    --rock: #7d7f86;
    --earth: #9a6232;
    --earth-dark: #4f3220;
    --white: #ffffff;
    --ring: rgba(255,255,255,0.85);
  }
  html, body {
    margin: 0;
    padding: 0;
    width: 1200px;
    height: 1155px;
    overflow: hidden;
    background: var(--stage-bg);
  }
  .canvas {
    position: relative;
    width: 1200px;
    height: 1155px;
  }
  .cover {
    position: absolute;
    left: 30px;
    top: 365px;
    width: 1140px;
    height: 424px;
    box-shadow: 0 22px 30px -18px rgba(0,0,0,0.4);
  }
  .cover svg { display: block; }
  .headline-light {
    font-family: "Open Sans", sans-serif;
    font-weight: 300;
    fill: var(--white);
  }
  .headline-bold {
    font-family: "Open Sans", sans-serif;
    font-weight: 800;
    fill: var(--white);
  }
  .brand-name {
    font-family: "Open Sans", sans-serif;
    font-weight: 700;
    fill: var(--white);
  }
</style>
</head>
<body>
<main class="canvas">
  <section class="cover" aria-label="Corvane Global Treks Facebook cover">
    <svg width="1140" height="424" viewBox="0 0 1140 424">
      <defs>
        <linearGradient id="scene-base" x1="0.1" y1="0" x2="0.35" y2="1">
          <stop offset="0" stop-color="var(--sky-deep)"/>
          <stop offset="0.22" stop-color="var(--sky-top)"/>
          <stop offset="0.4" stop-color="var(--sky-mid)"/>
          <stop offset="0.55" stop-color="var(--snow)"/>
          <stop offset="0.68" stop-color="var(--rock)"/>
          <stop offset="0.82" stop-color="var(--earth)"/>
          <stop offset="1" stop-color="var(--earth-dark)"/>
        </linearGradient>
        <radialGradient id="scene-glow" cx="0.45" cy="0.45" r="0.45">
          <stop offset="0" stop-color="#ffffff" stop-opacity="0.55"/>
          <stop offset="1" stop-color="#ffffff" stop-opacity="0"/>
        </radialGradient>
        <radialGradient id="scene-corner" cx="1" cy="1" r="0.6">
          <stop offset="0" stop-color="#3a3f52" stop-opacity="0.55"/>
          <stop offset="1" stop-color="#3a3f52" stop-opacity="0"/>
        </radialGradient>
        <linearGradient id="teal-panel" x1="0" y1="0" x2="1" y2="1">
          <stop offset="0" stop-color="var(--teal-dark)"/>
          <stop offset="1" stop-color="var(--teal-light)"/>
        </linearGradient>
        <radialGradient id="monastery-photo" cx="0.45" cy="0.55" r="0.7">
          <stop offset="0" stop-color="#c9b9a0"/>
          <stop offset="0.35" stop-color="#8a5a3c"/>
          <stop offset="0.7" stop-color="#4f5a2c"/>
          <stop offset="1" stop-color="#2e3a22"/>
        </radialGradient>
        <linearGradient id="summit-photo" x1="0.2" y1="0" x2="0.4" y2="1">
          <stop offset="0" stop-color="#4e74c0"/>
          <stop offset="0.3" stop-color="#c9d6ec"/>
          <stop offset="0.5" stop-color="#f2f5fa"/>
          <stop offset="0.75" stop-color="#9a958c"/>
          <stop offset="1" stop-color="#55514a"/>
        </linearGradient>
      </defs>

      <g class="scene-photo" role="img" aria-label="Snow-capped Himalayan peak above a brown river valley under a blue sky">
        <rect x="480" y="0" width="660" height="424" fill="url(#scene-base)"/>
        <rect x="480" y="0" width="660" height="424" fill="url(#scene-glow)"/>
        <rect x="480" y="0" width="660" height="424" fill="url(#scene-corner)"/>
      </g>

      <path class="teal-panel" d="M0 0 H522 C488 130 500 300 516 424 H0 Z" fill="url(#teal-panel)"/>

      <circle cx="421" cy="124" r="108" fill="none" stroke="var(--ring)" stroke-width="1.2"/>
      <circle class="photo-monastery" cx="421" cy="124" r="98" fill="url(#monastery-photo)"
              role="img" aria-label="Cliffside monastery with colourful prayer flags"/>

      <circle cx="484" cy="287" r="132" fill="none" stroke="var(--ring)" stroke-width="1.2"/>
      <circle class="photo-summit" cx="484" cy="287" r="123" fill="url(#summit-photo)"
              role="img" aria-label="Trekkers on a rocky ridge below snowy summits"/>

      <text class="headline-light" x="58" y="91" font-size="44" textLength="175" lengthAdjust="spacingAndGlyphs">VISIT THE</text>
      <text class="headline-bold" x="58" y="146" font-size="54" textLength="106" lengthAdjust="spacingAndGlyphs">TOP</text>
      <text class="headline-light" x="58" y="197" font-size="44" textLength="137" lengthAdjust="spacingAndGlyphs">OF THE</text>
      <text class="headline-bold" x="58" y="256" font-size="54" textLength="202" lengthAdjust="spacingAndGlyphs">WORLD</text>
      <text class="headline-light" x="58" y="306" font-size="44" textLength="227" lengthAdjust="spacingAndGlyphs">CHALLENGE</text>
      <text class="headline-bold" x="58" y="364" font-size="54" textLength="272" lengthAdjust="spacingAndGlyphs">YOURSELF</text>

      <g class="brand">
        <circle cx="924" cy="64" r="29" fill="none" stroke="var(--white)" stroke-width="3"/>
        <text class="brand-name" x="962" y="72" font-size="32" textLength="132" lengthAdjust="spacingAndGlyphs">CORVANE</text>
        <text class="brand-name" x="963" y="90" font-size="10" textLength="130" lengthAdjust="spacingAndGlyphs">GLOBAL TREKS</text>
      </g>
    </svg>
  </section>
</main>
</body>
</html>
```